Hockey Youth Club - Complete HP Design

I need a complete homepage design for a new youth hockey club. There are already some elements that can be used. For more information, please visit this products webpage. This site is currently unavailable for purchase at this time (Current) -) Team (Players, Coaches, Crew) -) Club (Philiosophy , Rules, Management Board, ....) -) Partners (Sponsors, Partners, ...)) Contact (Contact details, Callback Button) -) Shop (in the beginning view of products - further planned as online shop ) -) .... probably 2-3 more -) Footer with social media info, ..... Homepages from other youth hockey clubs (ex. Www.plo. At - this is what I am looking for in my life - BUT we dont want to copy them !!! Im interested in new and innovative designs.
Updates

Project Deadline Extended
Reason: Too much Wordpress - no innovation - please offer more designs in dark concept. At the moment the design is too decent - we are looking for sporty, active and fresh design. Thank you

Target Market(s)

Youth Hockey Players Parents

Industry/Entity Type

Club

Number of Pages Required

5+ page

Colors
fbed38
9d9d9d
1b1b1b
f5f5f5
ffffff

Requirements
Must have
• Clearline, modern design,
Nice to have
• Flashing elements (maybe the scratches fading in ...)
Should not have
• chaos

```html
<!DOCTYPE html>
<html lang="en">
<head>
<meta charset="utf-8">
<title>Frostbacks Youth Hockey Club</title>
<link rel="stylesheet" href="https://fonts.googleapis.com/css2?family=Saira+Condensed:wght@500;600;700&family=Open+Sans:wght@400;600&display=swap">
<style>
:root{
  --orange:#f3a930;
  --red:#e2282c;
  --ink:#1b1b1b;
  --grey:#9d9d9d;
  --text:#555555;
  --paper:#ffffff;
  --mist:#f5f5f5;
  --ice-a:#e6e9ed;
  --ice-b:#f7f8f9;
  --jersey-blue:#2c4790;
  --jersey-yellow:#eec23a;
  --jersey-red:#c9323b;
  --arena:#18264a;
}
*{margin:0;padding:0;box-sizing:border-box}
html,body{width:1200px;height:3442px;overflow:hidden;background:var(--paper)}
body{position:relative;font-family:"Open Sans",sans-serif;color:var(--text)}
.abs{position:absolute}
.head{font-family:"Saira Condensed",sans-serif;font-weight:700;text-transform:uppercase;color:var(--ink);line-height:1}
.head span{color:var(--orange)}
.btn{position:absolute;display:flex;align-items:center;justify-content:center;border-radius:20px;font-family:"Saira Condensed",sans-serif;font-weight:700;font-size:17px;text-transform:uppercase;color:#fff;letter-spacing:.3px}
.btn-red{background:var(--red)}
.btn-orange{background:var(--orange)}
.para{font-size:13.5px;line-height:21px;text-align:justify}

/* hero */
.hero{position:absolute;left:0;top:0;width:1200px;height:770px;background:linear-gradient(160deg,var(--ice-a),var(--ice-b) 60%,#e1e4e8)}
.hero-photo{position:absolute;left:400px;top:120px;width:790px;height:620px;
  background:linear-gradient(112deg,rgba(226,230,235,0) 0%,#dfe3e8 14%,#f2f3f5 22%,#2c4790 34%,#eec23a 44%,#f0c940 50%,#2c4790 60%,#c9323b 72%,#e9ecef 86%,rgba(233,236,239,0) 100%);
  -webkit-mask-image:radial-gradient(ellipse 60% 55% at 52% 48%,#000 55%,transparent 100%);
  mask-image:radial-gradient(ellipse 60% 55% at 52% 48%,#000 55%,transparent 100%)}
.logo{position:absolute;left:88px;top:44px;display:flex;align-items:center;gap:12px}
.logo-dot{width:56px;height:56px;border-radius:50%;background:var(--orange)}
.logo-name{font-family:"Saira Condensed",sans-serif;font-weight:700;font-size:28px;color:var(--ink);text-transform:uppercase}
.nav{position:absolute;left:434px;top:60px;display:flex;gap:32px;align-items:center;font-family:"Saira Condensed",sans-serif;font-weight:600;font-size:17px;text-transform:uppercase;color:var(--ink)}
.nav .active{color:var(--orange)}
.nav .signup{background:var(--red);color:#fff;border-radius:8px;padding:4px 32px;margin-left:-8px}
.hero-title{position:absolute;left:90px;top:350px;font-family:"Saira Condensed",sans-serif;font-weight:700;font-size:50px;color:var(--red);text-transform:uppercase;line-height:1}
.hero-sub{position:absolute;left:92px;top:405px;font-family:"Saira Condensed",sans-serif;font-weight:600;font-size:27px;color:var(--ink)}
.dots{position:absolute;left:92px;top:514px;display:flex;gap:6px}
.dots i{width:22px;height:22px;border-radius:50%;background:#5b5b5b;display:flex;align-items:center;justify-content:center}

.photo{position:absolute}
.frame{position:absolute;border:1.5px solid var(--red)}

/* team */
.card{position:absolute;top:1324px;width:290px;height:266px;background:#fff;box-shadow:0 2px 8px rgba(0,0,0,.12)}
.card-img{width:100%;height:158px}
.card h3{margin-top:20px;text-align:center;font-weight:400;font-size:17px;color:var(--ink);text-transform:uppercase}
.card p{margin:10px 24px 0;text-align:center;font-size:11.5px;line-height:17px;color:var(--grey)}

/* news */
.news-card{position:absolute;top:2410px;width:496px;height:170px;background:#fff;display:flex;box-shadow:0 2px 8px rgba(0,0,0,.1)}
.news-img{width:162px;height:170px;flex:none}
.news-body{padding:22px 22px 0 24px}
.news-body h4{font-weight:400;font-size:14.5px;color:var(--ink)}
.news-body .date{font-size:11.5px;color:var(--ink);margin-top:6px}
.news-body p{font-size:11.5px;line-height:17px;color:var(--ink);margin-top:4px}
.news-body .more{font-size:11.5px;color:var(--red);margin-top:4px}

/* partners */
.badge{position:absolute;top:2880px;width:172px;height:100px;border:1px solid #e2e2e2;border-radius:4px;background:var(--mist);display:flex;align-items:center;justify-content:center}
.badge i{width:90px;height:18px;background:#c4c4c4;border-radius:3px}

/* footer */
.foot-h{font-family:"Saira Condensed",sans-serif;font-weight:700;font-size:16px;color:var(--ink);text-transform:uppercase}
.foot-t{font-size:11.5px;line-height:20px;color:#666}
.social{display:flex;gap:10px}
.social i{width:22px;height:22px;background:#555;border-radius:3px}
</style>
</head>
<body>

<section class="hero">
  <div class="hero-photo" role="img" aria-label="Three youth hockey players in blue, yellow and red jerseys skating forward with sticks"></div>
  <svg class="abs" style="left:0;top:0" width="1200" height="770" viewBox="0 0 1200 770"><polygon points="0,760 1200,550 1200,770 0,770" fill="#fff"/></svg>
  <div class="logo"><div class="logo-dot"></div><div class="logo-name">Frostbacks</div></div>
  <nav class="nav">
    <span class="active">Home</span><span>News</span><span>Team</span><span>Club</span><span>Partners</span><span>Shop</span><span>Contact</span><span class="signup">Sign up</span>
  </nav>
  <h1 class="hero-title">Youth Hockey Club</h1>
  <p class="hero-sub">Neque porro quisquam dolorem ipsum</p>
  <div class="btn btn-orange" style="left:88px;top:450px;width:150px;height:40px">Get started</div>
  <div class="dots">
    <i><svg width="10" height="10" viewBox="0 0 10 10"><path d="M6.5 1.5 3 5l3.5 3.5" stroke="#fff" stroke-width="1.8" fill="none"/></svg></i>
    <i><svg width="10" height="10" viewBox="0 0 10 10"><path d="M3.5 1.5 7 5 3.5 8.5" stroke="#fff" stroke-width="1.8" fill="none"/></svg></i>
  </div>
</section>

<section class="club">
  <div class="frame" style="left:156px;top:815px;width:335px;height:321px"></div>
  <div class="photo" style="left:120px;top:792px;width:332px;height:321px;background:linear-gradient(172deg,#131f40 0%,#2f4f86 24%,#7d2630 44%,#3a3f52 56%,#b9c6d4 70%,#eef2f6 100%)" role="img" aria-label="Two hockey players battling for the puck under arena lights"></div>
  <h2 class="head abs" style="left:523px;top:842px;font-size:36px">Our <span>Club</span></h2>
  <p class="para abs" style="left:523px;top:893px;width:540px">It is a long established fact that a reader will be distracted by the readable content of a page when looking at its layout. The point of using Lorem Ipsum is that it has a more-or-less normal distribution of letters, as opposed to using 'Content here, content here', making it look like readable English. Many desktop publishing packages and web page editors now use Lorem Ipsum as their default model text, and a search for 'lorem ipsum' will uncover many web sites still in their infancy.</p>
  <div class="btn btn-red" style="left:523px;top:1048px;width:116px;height:34px;font-size:15px">Read more</div>
</section>

<svg class="abs" style="left:0;top:1190px" width="1200" height="610" viewBox="0 0 1200 610"><polygon points="0,0 1200,0 1200,600 0,415" fill="#f2f2f2"/></svg>
<h2 class="head abs" style="left:0;top:1245px;width:1200px;text-align:center;font-size:36px">Our <span>Team</span></h2>
<div class="card" style="left:126px"><div class="card-img" style="background:linear-gradient(180deg,#5a6679 0%,#8e9bb0 28%,#b2333c 46%,#3a3d4a 60%,#dfe5ec 78%,#f3f5f7 100%)" role="img" aria-label="Youth players chasing the puck"></div><h3>Players</h3><p>It has survived not only five centuries, but also the leap into electronic</p></div>
<div class="card" style="left:448px"><div class="card-img" style="background:linear-gradient(180deg,#3c4e6c 0%,#7b8ea8 26%,#e2b43a 44%,#f2f3f5 56%,#c9d3de 74%,#eef2f6 100%)" role="img" aria-label="Two players at a face-off"></div><h3>Coaches</h3><p>It has survived not only five centuries, but also the leap into electronic</p></div>
<div class="card" style="left:771px"><div class="card-img" style="background:linear-gradient(180deg,#4a5a3c 0%,#7f9a6a 24%,#c42c35 44%,#262a36 58%,#dbe2ea 76%,#f3f5f7 100%)" role="img" aria-label="Players skating during a match"></div><h3>Crew</h3><p>It has survived not only five centuries, but also the leap into electronic</p></div>

<section class="products">
  <h2 class="head abs" style="left:118px;top:1878px;font-size:36px">Our <span>Products</span></h2>
  <p class="para abs" style="left:120px;top:1928px;width:540px">It is a long established fact that a reader will be distracted by the readable content of a page when looking at its layout. The point of using Lorem Ipsum is that it has a more-or-less normal distribution of letters, as opposed to using 'Content here, content here', making it look like readable English. Many desktop publishing packages and web page editors now use Lorem Ipsum as their default model text, and a search for 'lorem ipsum' will uncover many web sites still in their infancy.</p>
  <div class="btn btn-red" style="left:120px;top:2085px;width:115px;height:34px;font-size:15px">Buy now</div>
  <div class="frame" style="left:700px;top:1870px;width:333px;height:315px"></div>
  <div class="photo" style="left:735px;top:1840px;width:330px;height:317px;background:#fff;border:1px solid #e3e3e3"></div>
  <div class="photo" style="left:752px;top:1862px;width:296px;height:272px;background:linear-gradient(150deg,#ffffff 0%,#2a2c33 22%,#6f7480 36%,#f4f4f6 48%,#c7262e 62%,#2a4aa0 74%,#f5f5f7 88%,#ffffff 100%)" role="img" aria-label="Hockey helmet, skates, gloves and puck on white"></div>
</section>

<svg class="abs" style="left:0;top:2253px" width="1200" height="505" viewBox="0 0 1200 505"><polygon points="0,0 1200,0 1200,375 0,502" fill="#f3a930"/></svg>
<h2 class="head abs" style="left:0;top:2318px;width:1200px;text-align:center;font-size:34px;color:#fff">Latest News</h2>
<svg class="abs" style="left:92px;top:2326px" width="16" height="22" viewBox="0 0 16 22"><path d="M11 3 4 11l7 8" stroke="#fff" stroke-width="2.5" fill="none"/></svg>
<svg class="abs" style="left:1084px;top:2326px" width="16" height="22" viewBox="0 0 16 22"><path d="M5 3l7 8-7 8" stroke="#fff" stroke-width="2.5" fill="none"/></svg>
<article class="news-card" style="left:87px">
  <div class="news-img" style="background:linear-gradient(180deg,#20273a 0%,#4a5878 26%,#c22f39 48%,#1b1e28 70%,#3b4356 100%)" role="img" aria-label="Player celebrating on the ice"></div>
  <div class="news-body"><h4>Nemo Enim Ipsam Volup</h4><div class="date">09-07-2017</div><p>Lorem Ipsum has been the industry's standard dummy text ever since the 1500s, when an unknown printer took a galley of type and scrambled it to make</p><div class="more">Read More &gt;&gt;</div></div>
</article>
<article class="news-card" style="left:613px">
  <div class="news-img" style="background:linear-gradient(180deg,#b7935c 0%,#d8c9a8 24%,#f4f5f7 42%,#2d4a8e 58%,#c6d0dc 76%,#eef1f4 100%)" role="img" aria-label="Player skating with the puck"></div>
  <div class="news-body"><h4>Nemo Enim Ipsam Volup</h4><div class="date">09-07-2017</div><p>Lorem Ipsum has been the industry's standard dummy text ever since the 1500s, when an unknown printer took a galley of type and scrambled it to make</p><div class="more">Read More &gt;&gt;</div></div>
</article>

<h2 class="head abs" style="left:0;top:2803px;width:1200px;text-align:center;font-size:34px;color:#3a3a3a">Partners</h2>
<div class="badge" style="left:147px"><i></i></div>
<div class="badge" style="left:331px"><i></i></div>
<div class="badge" style="left:515px"><i></i></div>
<div class="badge" style="left:699px"><i></i></div>
<div class="badge" style="left:883px"><i></i></div>

<svg class="abs" style="left:0;top:3035px" width="1200" height="407" viewBox="0 0 1200 407"><polygon points="0,5 1200,110 1200,407 0,407" fill="#f2f2f2"/></svg>
<footer>
  <div class="abs" style="left:88px;top:3200px;display:flex;align-items:center;gap:10px">
    <div style="width:52px;height:52px;border-radius:50%;background:var(--orange)"></div>
    <div class="logo-name" style="font-size:24px">Frostbacks</div>
  </div>
  <div class="abs" style="left:321px;top:3196px;width:230px">
    <div class="foot-h">Contact us</div>
    <div class="foot-t" style="margin-top:10px">Address : 12 Harbour Lane, Northfield,<br>NF4 2KD<br>Phone : 555-014-2290<br>Email : hello@frostbacks-club.org</div>
  </div>
  <div class="abs" style="left:647px;top:3196px;width:230px">
    <div class="foot-h">Sign up for newsletter</div>
    <div class="foot-t" style="margin-top:10px;line-height:17px">Your about us information would fit here nicely.</div>
    <div style="display:flex;margin-top:10px">
      <div style="width:145px;height:30px;background:#fff;border:1px solid #ddd;font-size:11px;padding:7px 8px;color:#888">Email address</div>
      <div style="width:58px;height:30px;background:var(--red);color:#fff;font-size:11px;display:flex;align-items:center;justify-content:center">Submit</div>
    </div>
  </div>
  <div class="abs" style="left:955px;top:3196px">
    <div class="foot-h">Follow us out there</div>
    <div class="social" style="margin-top:20px"><i></i><i></i><i></i><i></i></div>
  </div>
  <div class="abs" style="left:92px;top:3368px;width:1016px;height:1px;background:#d8d8d8"></div>
  <div class="abs foot-t" style="left:0;top:3384px;width:1200px;text-align:center;color:#333">Copyright © 2017. All Rights Reserved</div>
</footer>

</body>
</html>
```